Legal Service Estimated Retainer and Average Case Value

We need an 11x14 flyer that contains the standard retainers and average cost be case, both provided in documents, for each case type we handle. We need the information displayed, preferably in a way that makes the information readable but less troubling to a client shocked at price of litigation. We need one sheet with the retainers and average case value merged into one table.

Target Market(s)

Potential Clients

Font styles to use
Serif
Sans Serif

```html
<!DOCTYPE html>
<html lang="en">
<head>
<meta charset="utf-8">
<title>Retainers and Total Estimated Case Costs</title>
<link href="https://fonts.googleapis.com/css2?family=EB+Garamond:wght@400;500&family=Open+Sans:wght@400;600&display=swap" rel="stylesheet">
<style>
  :root {
    --navy: #0b1640;
    --ink: #1f2430;
    --rule-blue: #8296d4;
    --band-blue: #8ea2db;
    --row-grey: #e2e3e5;
    --header-grey: #dcdddf;
    --divider: #c9cacd;
    --page-bg: #ffffff;
    --canvas-bg: #f4f4f5;
  }
  * { margin: 0; padding: 0; box-sizing: border-box; }
  html, body { width: 1049px; height: 1200px; overflow: hidden; background: var(--canvas-bg); }
  .flyer {
    position: absolute; left: 84px; top: 40px;
    width: 880px; height: 1120px;
    background: var(--page-bg);
    font-family: "Open Sans", Arial, sans-serif;
    color: var(--ink);
  }
  .flyer-header {
    position: absolute; left: 0; top: 0; width: 100%; height: 152px;
    background: linear-gradient(to bottom, var(--header-grey), #ffffff);
  }
  .brand {
    position: absolute; left: 175px; top: 70px;
    display: flex; align-items: center; gap: 18px;
  }
  .brand-mark { width: 22px; height: 22px; background: var(--navy); }
  .brand-name {
    font-family: "EB Garamond", Georgia, serif;
    font-weight: 500; font-size: 38px; letter-spacing: 0.5px;
    color: var(--navy); text-transform: uppercase; line-height: 1;
  }
  .intro {
    position: absolute; left: 86px; top: 209px; width: 708px;
    font-family: "EB Garamond", Georgia, serif;
    font-size: 18.5px; line-height: 23px; text-indent: 56px;
    text-align: justify; color: #222;
  }
  .table-title {
    position: absolute; left: 0; top: 303px; width: 100%;
    text-align: center; font-weight: 600; font-size: 15.5px;
    text-decoration: underline; color: #2a2e38;
  }
  .fee-table {
    position: absolute; left: 87px; top: 334px; width: 705px;
    border-collapse: collapse; border-top: 2px solid #e4e5e7;
  }
  .fee-table td { height: 50.6px; font-size: 14px; font-weight: 600; vertical-align: middle; }
  .fee-table .case-type { width: 529px; padding-left: 14px; border-right: 2px solid var(--divider); }
  .fee-table .fee { text-align: center; font-weight: 400; }
  .fee-table tr:nth-child(odd) td { background: linear-gradient(to bottom, #ffffff 30%, var(--row-grey)); border-bottom: 1.5px solid var(--rule-blue); }
  .fee-table tr:nth-child(even) td { background: linear-gradient(to bottom, #ffffff 25%, var(--band-blue)); }
  .fee-table tr:last-child td { border-bottom: none; }
  .fee-note {
    position: absolute; left: 618px; top: 995px; width: 176px;
    text-align: center; font-size: 13.5px;
  }
  .flyer-footer {
    position: absolute; left: 0; top: 1037px; width: 100%; height: 54px;
    background: var(--navy); color: #fff;
    font-size: 19.5px; display: flex; align-items: center;
  }
  .footer-phone { position: absolute; left: 101px; }
  .footer-address { position: absolute; left: 287px; }
</style>
</head>
<body>
<main class="flyer">
  <div class="flyer-header"></div>
  <div class="brand">
    <span class="brand-mark"></span>
    <span class="brand-name">The Law Office of Morgan T Whitfield</span>
  </div>
  <p class="intro">In order for our clients to set expectations for legal fees, we provide the national average range of fees per case type.&nbsp; These are only to provide you with an understanding of what other cases have cost clients in similar cases.&nbsp; Please note these are not estimates nor guarantees of your own legal costs.</p>
  <h2 class="table-title">Retainers and Total Estimated Case Costs:</h2>
  <table class="fee-table">
    <tr><td class="case-type">Divorce (3301 C)</td><td class="fee">$2,000</td></tr>
    <tr><td class="case-type">Divorce (3301 D)</td><td class="fee">$2,500</td></tr>
    <tr><td class="case-type">Divorce and Custody</td><td class="fee">$3,500</td></tr>
    <tr><td class="case-type">Divorce and Equitable Distribution</td><td class="fee">$3,500</td></tr>
    <tr><td class="case-type">Divorce and Support</td><td class="fee">$3,000</td></tr>
    <tr><td class="case-type">Divorce, Custody and Support</td><td class="fee">$3,500</td></tr>
    <tr><td class="case-type">Divorce, Equitable Distribution and Support</td><td class="fee">$3,500</td></tr>
    <tr><td class="case-type">Divorce, Equitable Distribution and Custody</td><td class="fee">$5,000</td></tr>
    <tr><td class="case-type">Divorce, Equitable Distribution, Custody and Support</td><td class="fee">$3,500</td></tr>
    <tr><td class="case-type">Custody Initial Order</td><td class="fee">$3,000</td></tr>
    <tr><td class="case-type">Custody Modification</td><td class="fee">$3,500</td></tr>
    <tr><td class="case-type">Custody and Suppor</td><td class="fee">$3,000</td></tr>
    <tr><td class="case-type">(PFA) Protection From Abuse</td><td class="fee">$2,000</td></tr>
  </table>
  <p class="fee-note">Paid In Full</p>
  <footer class="flyer-footer">
    <span class="footer-phone">(555) 214-0386</span>
    <span class="footer-address">2750 Maple Ridge Road Suite 210, Fairview, PA 17000</span>
  </footer>
</main>
</body>
</html>
```